Business Card Design

We need a business card designed to portray the message that we are wedding and event stylists. We set up garden ceremonies and style wedding reception venues with chair covers and sashes, backdrops and draping's, wishing wells, tealight holders, table centerpieces. We also style corporate functions - Christmas parties, gala dinners, school formals, award nights. The colour of our uniforms are black and hot pink, if these colours could be incorporated. We would like to be able to use this design for letterhead, flyers and postcards etc. We would like the design to portray a professional, classic image that would relate to both spectrums of our business, weddings and corporate events. If you could develop a logo to incorporate would be great

Target Market(s)

brides, corporate compaines

Industry/Entity Type

Wedding

Contact Information for Business Card

Velvet Crest Occasions & Party Hire
Phone: 0417 553 916 Email:vcoph@fernmail.example
Web: www.velvetcrestoccasions.example.au

Requirements
Must have
• Must include that we set up for weddings, engagements, birthdays, anniversaries, corporate functions, school formals, any occasion.

```html
<!DOCTYPE html>
<html lang="en">
<head>
<meta charset="utf-8">
<title>Velvet Crest Occasions &amp; Party Hire – Business Card</title>
<link rel="stylesheet" href="https://fonts.googleapis.com/css2?family=Pinyon+Script&family=Questrial&display=swap">
<style>
  :root {
    --page: #f4f2ef;
    --card-cream: #f3e4cc;
    --card-cream-deep: #ead5b4;
    --band-cream: #f8ecda;
    --gold: #b98a2e;
    --gold-light: #e3c46a;
    --gold-dark: #8a6418;
    --ink: #2b241d;
    --ink-script: #3a2b1c;
  }
  * { margin: 0; padding: 0; box-sizing: border-box; }
  html, body {
    width: 1200px; height: 900px; overflow: hidden;
    background: var(--page);
  }
  .canvas {
    position: relative; width: 1200px; height: 900px;
    display: flex; align-items: center; justify-content: center;
  }
  .business-card {
    position: relative; width: 1000px; height: 572px;
    border-radius: 34px; overflow: hidden;
    box-shadow: 0 10px 30px rgba(0,0,0,0.12);
  }
  .card-background {
    position: absolute; inset: 0;
    background: radial-gradient(ellipse at 50% 45%, var(--card-cream) 0%, var(--card-cream-deep) 100%);
  }
  .services {
    position: absolute; top: 58px; left: 0; right: 0;
    text-align: center;
    font-family: "Questrial", sans-serif;
    font-size: 19px; line-height: 1.3;
    color: var(--gold);
  }
  .ornament {
    position: absolute; left: 50%; width: 250px; height: 78px;
    transform: translateX(-50%);
    background: radial-gradient(ellipse at 50% 50%, var(--gold-light) 0%, var(--gold) 45%, rgba(185,138,46,0) 72%);
    border-radius: 50%;
  }
  .ornament--top { top: 150px; }
  .ornament--bottom { top: 330px; }
  .name-band {
    position: absolute; left: 0; right: 0; top: 236px; height: 90px;
    background: var(--band-cream);
    border-top: 3px solid var(--gold);
    border-bottom: 3px solid var(--gold);
    display: flex; align-items: center; justify-content: center;
  }
  .name-band::before, .name-band::after {
    content: ""; position: absolute; left: 0; right: 0; height: 1px;
    background: var(--gold-light);
  }
  .name-band::before { top: 4px; }
  .name-band::after { bottom: 4px; }
  .business-name {
    font-family: "Pinyon Script", cursive;
    font-weight: 400; font-size: 52px;
    color: var(--ink-script);
    white-space: nowrap;
  }
  .contact-list {
    position: absolute; left: 50px; top: 418px;
    list-style: none;
    font-family: "Questrial", sans-serif;
    color: var(--ink);
  }
  .contact-item {
    display: flex; align-items: center; gap: 12px;
    height: 38px;
  }
  .contact-item--phone { font-size: 30px; }
  .contact-item--email { font-size: 27px; }
  .contact-item--web { font-size: 23px; }
  .contact-icon { width: 26px; height: 26px; flex: none; }
  .contact-icon path, .contact-icon rect, .contact-icon circle { fill: var(--gold); }
  .contact-icon .stroke { fill: none; stroke: var(--band-cream); stroke-width: 1.6; }
</style>
</head>
<body>
<main class="canvas">
  <article class="business-card">
    <div class="card-background" role="img" aria-label="Cream damask floral pattern covering the card"></div>

    <p class="services">we set up for weddings, engagements, birthdays,anniversaries,<br>corporate functions, school formals, any occasion.</p>

    <div class="ornament ornament--top" role="img" aria-label="Gold baroque flourish ornament above the name"></div>

    <header class="name-band">
      <h1 class="business-name">Velvet Crest Occasions &amp; Party Hire</h1>
    </header>

    <div class="ornament ornament--bottom" role="img" aria-label="Gold baroque flourish ornament below the name"></div>

    <ul class="contact-list">
      <li class="contact-item contact-item--phone">
        <svg class="contact-icon" viewBox="0 0 24 24" aria-hidden="true">
          <path d="M6.6 10.8a15.1 15.1 0 0 0 6.6 6.6l2.2-2.2a1 1 0 0 1 1-.25 11.4 11.4 0 0 0 3.6.6 1 1 0 0 1 1 1V20a1 1 0 0 1-1 1A17 17 0 0 1 3 4a1 1 0 0 1 1-1h3.5a1 1 0 0 1 1 1c0 1.25.2 2.45.6 3.6a1 1 0 0 1-.25 1z"/>
        </svg>
        <span>0417 553 916</span>
      </li>
      <li class="contact-item contact-item--email">
        <svg class="contact-icon" viewBox="0 0 24 24" aria-hidden="true">
          <rect x="2" y="5" width="20" height="14" rx="2"/>
          <path class="stroke" d="M3 6.5l9 7 9-7"/>
        </svg>
        <span>vcoph@fernmail.example</span>
      </li>
      <li class="contact-item contact-item--web">
        <svg class="contact-icon" viewBox="0 0 24 24" aria-hidden="true">
          <circle cx="12" cy="12" r="10"/>
          <path class="stroke" d="M2 12h20M12 2c3 3 3 17 0 20M12 2c-3 3-3 17 0 20M4 7h16M4 17h16"/>
        </svg>
        <span>www.velvetcrestoccasions.example.au</span>
      </li>
    </ul>
  </article>
</main>
</body>
</html>
```